Catalogue of basic beekeeping supplies, from a local Texas supplier

I need a roughly 20 page catalogue designed for a bee supplies company in Texas. It will feature a front page, with the company name, "Ridgewell Hive Goods" with the background being a cool beekeeping picture, which I can provide. The back cover will be info on where we are located, and how to contact us. The inside will be about 200 products. I've got the descriptions and pictures located in a online version of a parent catalogue, or you can view the attached pdf, in which I've market out the products not to include, and the ones that are left are the ones I need in the new catalogue. So, the designer will need to copy the descriptions and pictures of products from the parent catalogue, and paste them into this new catalogue. The parent catalogue has about 1000 items, but I've marked out the items I do not want in the new catalogue. Designer will also need to create an index in the back, and put our contact info on the bottom of each page: Ridgewell Hive Goods visit www.ridgewellhivegoods.example or call 555-318-2096 to order

Target Market(s)

18yrs-70yrs, Male & Female

Industry/Entity Type

It Company

Font styles to use
Serif
Sans Serif

Colors
fefbf1
fbed22
ffc214
fece3e
fee18a
fff3d1

Requirements
Must have
• Clean, organized, easy to read and find products.
Nice to have
• As few pages as possible, but still easy to read and not cluttered
Should not have
• Clutter, disorganized, overly colorful, childish

```html
<!DOCTYPE html>
<html lang="en">
<head>
<meta charset="utf-8">
<title>Ridgewell Hive Goods – Catalogue Contents Spread</title>
<link href="https://fonts.googleapis.com/css2?family=Quicksand:wght@500&family=Open+Sans:wght@400;700&family=Oswald:wght@500&display=swap" rel="stylesheet">
<style>
  :root{
    --backdrop:#dcdbd8;
    --paper:#ffffff;
    --gold:#c99326;
    --gold-light:#e2b24a;
    --charcoal:#3e3e41;
    --navy:#24406f;
    --photo-deep:#b99a2c;
    --photo-mid:#e0c23a;
    --photo-light:#f2dc6a;
    --white:#ffffff;
  }
  *{box-sizing:border-box;margin:0;padding:0}
  html,body{width:1200px;height:804px;overflow:hidden;background:var(--backdrop)}
  .spread{position:absolute;left:100px;top:50px;width:1000px;height:704px;display:flex;box-shadow:0 6px 24px rgba(0,0,0,.18)}
  .page{position:relative;width:500px;height:704px;overflow:hidden}

  /* left page */
  .page--feature{background:radial-gradient(ellipse at 45% 50%,var(--photo-light) 0%,var(--photo-mid) 45%,var(--photo-deep) 100%)}
  .feature-quote{position:absolute;left:86px;top:70px;width:320px;display:flex;gap:10px;color:var(--white);font-family:"Quicksand",sans-serif;font-weight:500}
  .feature-quote__mark{font-size:66px;line-height:.8;font-family:"Open Sans",sans-serif;font-weight:700}
  .feature-quote__text{font-size:14.5px;line-height:1.3;letter-spacing:.3px}

  /* right page */
  .page--contents{background:var(--paper)}
  .running-head{position:absolute;top:0;left:0;width:500px;height:60px}
  .running-head__rule{position:absolute;left:18px;top:44px;width:290px;height:1.5px;background:var(--charcoal)}
  .running-head__brand{position:absolute;left:318px;top:36px;display:flex;align-items:center;gap:5px;font-family:"Oswald",sans-serif;font-weight:500;font-size:10px;letter-spacing:.4px;color:var(--charcoal);text-transform:uppercase}
  .running-head__dot{width:9px;height:9px;border-radius:50%;background:var(--gold)}
  .running-head__tab{position:absolute;right:0;top:28px}

  .contents-title{position:absolute;left:138px;top:132px;font-family:"Open Sans",sans-serif;font-weight:400;font-size:38px;color:var(--navy);letter-spacing:.5px}

  .toc{position:absolute;left:112px;top:224px;list-style:none}
  .toc__item{position:relative;height:33px;width:330px}
  .toc__bar{position:absolute;left:32px;top:0;width:298px;height:21px;background:linear-gradient(90deg,var(--gold) 0%,var(--gold-light) 100%);border-radius:0 12px 12px 0;padding-left:10px;font-family:"Open Sans",sans-serif;font-size:9px;line-height:21px;color:rgba(255,255,255,.85)}
  .toc__num{position:absolute;left:0;top:9px;width:36px;height:24px;background:var(--charcoal);color:var(--white);font-family:"Open Sans",sans-serif;font-weight:700;font-size:16px;line-height:24px;text-align:center;border-radius:2px}

  .page-foot{position:absolute;left:0;bottom:0;width:500px;height:34px;display:flex}
  .page-foot__band{flex:1;background:var(--charcoal);display:flex;align-items:center;padding-left:18px;gap:64px}
  .page-foot__folio{width:18px;height:18px;border-radius:50%;border:2px solid var(--gold);background:var(--white);color:var(--charcoal);font-family:"Open Sans",sans-serif;font-weight:700;font-size:9px;display:flex;align-items:center;justify-content:center}
  .page-foot__contact{font-family:"Open Sans",sans-serif;font-size:7.5px;color:#b9b9bc;letter-spacing:.2px}
  .page-foot__social{width:128px;background:var(--gold);display:flex;align-items:center;justify-content:center;gap:9px}
  .page-foot__icon{width:11px;height:11px;border-radius:2px;background:var(--white);opacity:.85}
  .gutter{position:absolute;left:0;top:0;width:24px;height:704px;background:linear-gradient(90deg,rgba(0,0,0,.12),rgba(0,0,0,0))}
</style>
</head>
<body>
<main class="spread">
  <section class="page page--feature" role="img" aria-label="Close-up photograph of a honey bee carrying pollen, hovering over a yellow flower">
    <blockquote class="feature-quote">
      <span class="feature-quote__mark">“</span>
      <p class="feature-quote__text">Ridgewell Hive Goods offers a wide selection of quality beekeeping equipment, supplies and nucs at competitive prices.</p>
    </blockquote>
  </section>

  <section class="page page--contents">
    <div class="gutter"></div>
    <header class="running-head">
      <div class="running-head__rule"></div>
      <div class="running-head__brand"><span class="running-head__dot"></span>Ridgewell Hive Goods</div>
      <svg class="running-head__tab" width="60" height="16" viewBox="0 0 60 16">
        <polygon points="8,0 60,0 60,16 16,16" fill="#c99326"/>
        <polygon points="0,0 20,0 26,8 20,16 8,16 14,8" fill="#3e3e41"/>
        <path d="M17 5 L14 8 L17 11" stroke="#fff" stroke-width="1.5" fill="none"/>
      </svg>
    </header>

    <h1 class="contents-title">CONTENTS</h1>

    <ol class="toc">
      <li class="toc__item"><span class="toc__bar">About Us</span><span class="toc__num">03</span></li>
      <li class="toc__item"><span class="toc__bar">Est aute commos nullore volese modis dentibe</span><span class="toc__num">04</span></li>
      <li class="toc__item"><span class="toc__bar">Est aute commos nullore volese modis dentibe</span><span class="toc__num">05</span></li>
      <li class="toc__item"><span class="toc__bar">Est aute commos nullore volese modis dentibe</span><span class="toc__num">06</span></li>
      <li class="toc__item"><span class="toc__bar">Est aute commos nullore volese modis dentibe</span><span class="toc__num">07</span></li>
      <li class="toc__item"><span class="toc__bar">Est aute commos nullore volese modis dentibe</span><span class="toc__num">08</span></li>
      <li class="toc__item"><span class="toc__bar">Est aute commos nullore volese modis dentibe</span><span class="toc__num">09</span></li>
      <li class="toc__item"><span class="toc__bar">Est aute commos nullore volese modis dentibe</span><span class="toc__num">10</span></li>
    </ol>

    <footer class="page-foot">
      <div class="page-foot__band">
        <span class="page-foot__folio">5</span>
        <span class="page-foot__contact">info@ridgewellhivegoods.example &nbsp;|&nbsp; www.ridgewellhivegoods.example</span>
      </div>
      <div class="page-foot__social">
        <span class="page-foot__icon"></span><span class="page-foot__icon"></span><span class="page-foot__icon"></span><span class="page-foot__icon"></span>
      </div>
    </footer>
  </section>
</main>
</body>
</html>
```